Morvek Menu

Hi there,
My restaurant called "Morvek" means Spice in hebrew.
We are middle eastern restaurant that specialist in dips,salads and hot bread baked on the spot and charcoal grilled meat skewers
The restaurant is pretty casual and the atmosphere is nice and customers feels like home.
on www.morvek.com.au you can see photos of the restaurant and the food.
ill add up the menus that i would like to be design please and the logo that is on the front of the shop is been add up
thank you

Target Market(s)

The regulars of the restaurant is jewish/israelis

Industry/Entity Type

Restaurant

```html
<!DOCTYPE html>
<html lang="en">
<head>
<meta charset="utf-8">
<title>Morvek Menu</title>
<link href="https://fonts.googleapis.com/css2?family=Marcellus&family=Lustria&family=Open+Sans:wght@600;700&display=swap" rel="stylesheet">
<style>
  :root {
    --backdrop: #e6e6e6;
    --paper: #ffffff;
    --ink: #2e2e2e;
    --ink-soft: #7a7a7a;
    --brand-red: #c0273a;
    --bar: #3d3d3f;
    --bar-text: #ffffff;
    --dot: #e8c33a;
  }
  * { box-sizing: border-box; margin: 0; padding: 0; }
  html, body { width: 1200px; height: 800px; overflow: hidden; }
  body {
    background: var(--backdrop);
    font-family: "Lustria", Georgia, serif;
    color: var(--ink);
    display: flex;
    gap: 20px;
    padding: 16px 24px;
  }
  .menu-page {
    flex: 1;
    min-width: 0;
    height: 768px;
    overflow: hidden;
    background: var(--paper);
    padding: 18px 26px 14px;
    display: flex;
    flex-direction: column;
    box-shadow: 0 2px 10px rgba(0,0,0,.12);
  }
  .page-header {
    display: flex;
    align-items: flex-end;
    justify-content: space-between;
    padding-bottom: 6px;
  }
  .page-title {
    font-family: "Marcellus", Georgia, serif;
    font-weight: 400;
    color: var(--brand-red);
    font-size: 34px;
    letter-spacing: 6px;
    line-height: 1;
  }
  .venue-details {
    border-left: 2px solid var(--ink);
    padding-left: 10px;
    font-size: 9.5px;
    line-height: 1.35;
    color: var(--ink-soft);
  }
  .dot-rule {
    display: flex;
    justify-content: space-between;
    padding: 2px 30px 4px;
  }
  .dot-rule i { width: 4px; height: 4px; border-radius: 50%; background: var(--ink); }
  .section-bar {
    background: var(--bar);
    color: var(--bar-text);
    font-family: "Open Sans", Arial, sans-serif;
    font-weight: 700;
    font-size: 11px;
    height: 16px;
    display: flex;
    align-items: center;
    justify-content: center;
    gap: 8px;
    margin: 5px 0 3px;
  }
  .section-bar::before, .section-bar::after {
    content: "";
    width: 5px; height: 5px;
    border-radius: 50%;
    background: var(--dot);
  }
  .section-note {
    font-size: 9px;
    color: var(--ink-soft);
    text-align: center;
    line-height: 1.25;
  }
  .items {
    display: grid;
    grid-template-columns: 1fr 1fr;
    column-gap: 24px;
    font-size: 11px;
    line-height: 1.3;
  }
  .items.single { grid-template-columns: 1fr; }
  .item { display: flex; justify-content: space-between; gap: 6px; }
  .item > span:first-child { white-space: nowrap; overflow: hidden; }
  .item small { font-size: 7.5px; color: var(--ink-soft); }
  .price { white-space: nowrap; }
  .fine-print { font-size: 8px; color: var(--ink-soft); line-height: 1.25; }
  .page-footer {
    margin-top: auto;
    text-align: center;
    font-size: 9.5px;
    line-height: 1.4;
    color: var(--ink);
  }
</style>
</head>
<body>

<article class="menu-page dinner-menu">
  <header class="page-header">
    <h1 class="page-title">Dinner Menu</h1>
    <p class="venue-details">412 Larkmere Road,<br>Elsbury South<br>Tel. 9410 3827</p>
  </header>

  <section class="menu-section">
    <h2 class="section-bar">Something to start with</h2>
    <div class="items">
      <div>
        <p class="item"><span>Salads &amp; Dips</span><span class="price">$5*</span></p>
        <p class="item"><span>Falafel Balls</span><span class="price">$8.50</span></p>
        <p class="item"><span>Moroccan Beef Cigars</span><span class="price"></span></p>
      </div>
      <div>
        <p class="item"><span>Fried Cauliflower</span><span class="price">$7*</span></p>
      </div>
    </div>
  </section>

  <section class="menu-section">
    <h2 class="section-bar">Salads &amp; Dips</h2>
    <div class="items">
      <div>
        <p class="fine-print">5 choices for $12 or 6 choices for $20</p>
        <p class="item"><span>Baba Ganoush*</span></p>
        <p class="item"><span>Chatzilim / Moroccan Tomato Salsa*</span></p>
        <p class="item"><span>Corn Salad*</span></p>
        <p class="item"><span>Mixed Pickles*</span></p>
        <p class="fine-print">*Let us know if you are looking for a starter or to accompany a Shashlik from the charcoal grill</p>
      </div>
      <div>
        <p class="item"><span>Moroccan Carrot*</span></p>
        <p class="item"><span>Roasted Beetroot*</span></p>
        <p class="item"><span>Hummus*</span></p>
        <p class="item"><span>Tahini*</span></p>
      </div>
    </div>
  </section>

  <section class="menu-section">
    <h2 class="section-bar">From the charcoal grill</h2>
    <div class="items">
      <div>
        <p class="item"><span>Chicken Shashlik</span><span class="price">$8.50*</span></p>
        <p class="item"><span>Lamb Shashlik</span><span class="price">$10*</span></p>
        <p class="item"><span>Chatzilim (Eggplant)</span><span class="price">$9*</span></p>
      </div>
      <div>
        <p class="item"><span>Kebab (Kofta) Shashlik</span><span class="price">$8.50*</span></p>
        <p class="item"><span>Chicken Liver</span><span class="price">$7.50*</span></p>
      </div>
    </div>
  </section>

  <section class="menu-section">
    <h2 class="section-bar">Hummus Plates</h2>
    <div class="items">
      <div>
        <p class="item"><span>Masabacha <small>– with Tahini and whole chickpeas*</small></span><span class="price">$12</span></p>
        <p class="item"><span>Ful <small>– served with fava beans</small></span><span class="price">$15</span></p>
      </div>
      <div>
        <p class="item"><span>Mushroom <small>– with pan fried mushrooms</small></span><span class="price">$15</span></p>
        <p class="item"><span>Basar <small>– served with mince meat</small></span><span class="price">$16.5</span></p>
      </div>
    </div>
  </section>

  <section class="menu-section">
    <h2 class="section-bar">Sides</h2>
    <div class="items">
      <div><p class="item"><span>Chips</span><span class="price">$8</span></p></div>
      <div><p class="item"><span>Israeli Salad</span><span class="price">$9</span></p></div>
    </div>
  </section>

  <section class="menu-section">
    <h2 class="section-bar">Desserts</h2>
    <div class="items">
      <div>
        <p class="item"><span>Malabi <small>(Rose water pudding, Rose syrup, Pistachios)</small></span><span class="price">$8</span></p>
        <p class="item"><span>Trio of Sorbet</span><span class="price">$9</span></p>
        <p class="item"><span>Turkish Delight Ice-cream</span><span class="price">$9</span></p>
      </div>
      <div>
        <p class="item"><span>Safta Rina's Semolina Cake</span><span class="price">$4.5</span></p>
        <p class="item"><span>Crème Brulee</span><span class="price">$9</span></p>
      </div>
    </div>
  </section>

  <section class="menu-section">
    <h2 class="section-bar">Plates</h2>
    <p class="section-note">All plates served with hummus, tahini, chips and Israeli salad</p>
    <div class="items">
      <div>
        <p class="item"><span>Falafel</span><span class="price">$18.5</span></p>
        <p class="item"><span>Schnitzel</span><span class="price">$20</span></p>
        <p class="item"><span>Chicken</span><span class="price">$21</span></p>
        <p class="item"><span>Liver</span><span class="price">$21</span></p>
      </div>
      <div>
        <p class="item"><span>Kofta</span><span class="price">$21</span></p>
        <p class="item"><span>Heart</span><span class="price">$21</span></p>
        <p class="item"><span>Lamb</span><span class="price">$22</span></p>
      </div>
    </div>
  </section>

  <section class="menu-section">
    <h2 class="section-bar">Kids (10 and under only)</h2>
    <div class="items">
      <div><p class="item"><span>Schnitzel Plate with salad and Chips</span><span class="price">$10</span></p></div>
      <div><p class="item"><span>Falafel Plate with salad and chips</span><span class="price">$9</span></p></div>
    </div>
  </section>

  <section class="menu-section">
    <h2 class="section-bar">Drinks</h2>
    <div class="items">
      <div>
        <p class="item"><span>Cola/Diet Cola/Cola Zero/Fizzo/Lemo</span><span class="price">$3</span></p>
        <p class="item"><span>Black Beer/Soda Water/Mineral Water</span><span class="price">$4</span></p>
        <p class="item"><span>Limonana <small>~Old Fashioned Lemonade, Mint glass</small></span><span class="price">$4</span></p>
        <p class="item"><span>Limonana <small>~Old Fashioned Lemonade, Mint jug</small></span><span class="price">$11</span></p>
      </div>
      <div>
        <p class="item"><span>Coffee/Chai/Hot Chocolate</span><span class="price">$3.5</span></p>
        <p class="item"><span>Turkish Coffee</span><span class="price">$3.5</span></p>
        <p class="item"><span>Tea with nana (fresh mint)</span><span class="price">$3.5</span></p>
        <p class="item"><span>Israeli Grape/ Israeli Strawberry Banana</span><span class="price">$4</span></p>
      </div>
    </div>
  </section>
</article>

<article class="menu-page takeaway-menu">
  <header class="page-header">
    <h1 class="page-title">Take Away Menu</h1>
    <p class="venue-details">412 Larkmere Road,<br>Elsbury South<br>Tel. 9410 3827</p>
  </header>
  <div class="dot-rule" aria-hidden="true"><i></i><i></i><i></i><i></i><i></i><i></i><i></i><i></i><i></i><i></i><i></i><i></i></div>

  <section class="menu-section">
    <h2 class="section-bar">Salads &amp; Dips</h2>
    <p class="section-note">Small $5.50 / Large $10.00 / Jumbo $16.00</p>
    <div class="items">
      <div>
        <p class="item"><span>Baba Ganoush (GF)</span></p>
        <p class="item"><span>Turkish (GF)</span></p>
        <p class="item"><span>Chatzilim (Fried Eggplant) (GF)</span></p>
        <p class="item"><span>Corn Salad (GF)</span></p>
        <p class="item"><span>Mixed Pickles (GF)</span></p>
      </div>
      <div>
        <p class="item"><span>Moroccan Carrot (GF)</span></p>
        <p class="item"><span>Roasted Beetroot (GF)</span></p>
        <p class="item"><span>Hummus (GF)</span></p>
        <p class="item"><span>Tahini (GF)</span></p>
        <p class="item"><span>White cabbage (GF)</span></p>
      </div>
    </div>
  </section>

  <section class="menu-section">
    <h2 class="section-bar">Hummus Plates</h2>
    <p class="section-note">Served with 1 Laffa and Pickles</p>
    <div class="items single">
      <p class="item"><span>Masabacha – served with tahini and whole chickpeas</span><span class="price">$12.00 (GF)</span></p>
      <p class="item"><span>Ful – served with Fava beans</span><span class="price">$15.00 (GF)</span></p>
      <p class="item"><span>Mushroom – served with Pan Fried Mushrooms</span><span class="price">$15.00 (GF)</span></p>
      <p class="item"><span>Basar – served with Mince Meat</span><span class="price">$16.50 (GF)</span></p>
    </div>
  </section>

  <section class="menu-section">
    <h2 class="section-bar">Laffa Wraps</h2>
    <p class="section-note">Served with Hummus, Tahini, Israeli Salad and Pickles<br>(One large skewer per serve)</p>
    <div class="items">
      <div>
        <p class="item"><span>Falafel</span><span class="price">$12.00</span></p>
        <p class="item"><span>Chicken Shashlik</span><span class="price">$14.00</span></p>
        <p class="item"><span>Lamb Shashlik</span><span class="price">$15.00</span></p>
      </div>
      <div>
        <p class="item"><span>Kofta</span><span class="price">$13.00</span></p>
        <p class="item"><span>Liver Shashlik</span><span class="price">$13.50</span></p>
        <p class="item"><span>Schnitzel</span><span class="price">$13.00</span></p>
      </div>
    </div>
  </section>

  <section class="menu-section">
    <h2 class="section-bar">From the charcoal grill</h2>
    <div class="items">
      <div>
        <p class="item"><span>Chicken Shashlik</span><span class="price">$8.50 (GF)</span></p>
        <p class="item"><span>Lamb Shashlik</span><span class="price">$9.50 (GF)</span></p>
        <p class="item"><span>Kofta (Lamb kebab) Shashlik</span><span class="price">$8.50 (GF)</span></p>
      </div>
      <div>
        <p class="item"><span>Liver Shashlik</span><span class="price">$8.50 (GF)</span></p>
        <p class="item"><span>Schnitzel</span><span class="price">$10.00</span></p>
      </div>
    </div>
  </section>

  <section class="menu-section">
    <h2 class="section-bar">Sides</h2>
    <div class="items">
      <div>
        <p class="item"><span>Chips</span><span class="price">$7.00</span></p>
        <p class="item"><span>Falafel Balls (6 per serve)</span><span class="price">$5.00</span></p>
      </div>
      <div>
        <p class="item"><span>Moroccan Beef Cigars</span><span class="price">$9.00</span></p>
        <p class="item"><span>Laffa</span><span class="price">$2.00</span></p>
      </div>
    </div>
  </section>

  <footer class="page-footer">
    <p>Morvek is able to provide catering for your Dinner parties / Shabbat dinners. For more information please contact us.</p>
    <p>Please Note</p>
    <p>Prices subject to change without notice.</p>
  </footer>
</article>

</body>
</html>
```